IT-Dienstleister für Projektmanagementsoftware sucht Broschüre im DIN-A4-Format
Zielgruppe
Wir sind ein IT-Dienstleister für Projektmanagementsoftware. Wir installieren, migrieren und entwickeln Software für das Projektmanagement auf Basis von Veltrona Technologien. Unsere Zielgruppe sind mittelständische Unternehmen und große Konzerne. Je komplexer das Projektmanagement in einem Unternehmen, desto eher helfen unsere Lösungen.
Aufgabenstellung
Es soll eine DIN A4 Hochglanz Broschüre für eine Messe entstehen. Wir haben bereits ein Grobkonzept mit Bildauswahl und Texten erstellt. An diesem soll sich orientiert werden. Bezüglich desDesigns, der Anordnung der Texte und Bilder etc. besteht völlige Freiheit. Weitere Orientierung bieten unsere Webseiten hollweckfeist.de und tivonet.de. Die Texte und Screenshots sind teilweise nur Platzhalter und müssen später noch angepasst werden können. Wir benötigen daher unbedingt die Rohdaten des Designs.

```html
<!DOCTYPE html>
<html lang="de">
<head>
<meta charset="utf-8">
<title>Hollweck &amp; Feist – Broschüre</title>
<link href="https://fonts.googleapis.com/css2?family=Raleway:wght@300;400&family=Roboto:wght@400;500&display=swap" rel="stylesheet">
<style>
:root{
  --stage:#e4e4e4;
  --paper:#ffffff;
  --paper-soft:#f1f1f1;
  --green:#8cc63e;
  --ink:#3a3a3a;
  --ink-soft:#6d6d6d;
  --line:#d6d6d6;
}
*{box-sizing:border-box;margin:0;padding:0}
html,body{width:1200px;height:3001px;overflow:hidden;background:var(--paper)}
body{font-family:"Roboto",Arial,sans-serif;color:var(--ink)}
.stage{position:relative;background:var(--stage);overflow:hidden}
.stage--cover{height:862px}
.stage--spread{height:689px;margin-top:24px}
.page{position:absolute;background:var(--paper);overflow:hidden}
.cover{left:320px;top:35px;width:560px;height:792px}
.spread{position:absolute;left:180px;top:48px;width:840px;height:594px;box-shadow:0 6px 18px rgba(0,0,0,.15)}
.spread .page{top:0;width:420px;height:594px}
.page--left{left:0}
.page--right{left:420px}
.fill{position:absolute;inset:0}
svg{display:block}
.brand-name{position:absolute;font-family:"Raleway",sans-serif;font-weight:400;color:var(--ink);white-space:nowrap}
.cover .brand-name{right:40px;top:40px;font-size:22px}
.cover__title{position:absolute;left:56px;top:470px;font-family:"Raleway",sans-serif;font-weight:300;font-size:30px;line-height:1.22;color:#fff}
.accent{color:var(--green)}
.intro__text{position:absolute;left:174px;top:318px;font-family:"Raleway",sans-serif;font-weight:400;font-size:17px;line-height:1.3;color:var(--ink)}
.partner{bottom:22px;font-size:13px}
.partner--tivo{left:120px}
.partner--hf{right:30px}
.product{position:absolute;left:52px;right:34px;color:#fff}
.product__name{font-family:"Raleway",sans-serif;font-weight:300;font-size:35px;letter-spacing:.01em}
.product__lead{font-size:11px;line-height:1.35;margin-top:10px;color:#f4f9ec}
.product__body{font-size:8px;line-height:1.45;margin-top:26px;color:#2d3a1b}
.product__body p+p{margin-top:9px}
.page--panel{background:var(--paper-soft)}
.card{position:absolute;left:40px;width:350px;background:var(--paper);box-shadow:0 1px 4px rgba(0,0,0,.12)}
.card__text{position:absolute;left:16px;top:36px;width:120px;font-size:7.5px;line-height:1.35;color:var(--ink)}
.card__text ul{list-style:none;margin-top:8px}
.card__text li::before{content:"» ";color:var(--ink-soft)}
.card__art{position:absolute;right:12px;top:10px}
.mini{font-family:"Roboto",sans-serif;font-size:4.5px;fill:var(--ink-soft)}
.bullets{position:absolute;top:24px;left:24px;right:24px;display:flex;gap:24px;font-size:7.5px;line-height:1.35}
.bullets ul{list-style:none;flex:1}
.bullets li::before{content:"» ";color:var(--ink-soft)}
.bullets li{margin-bottom:6px}
</style>
</head>
<body>

<section class="stage stage--cover">
  <div class="page cover">
    <svg class="fill" width="560" height="792" role="img" aria-label="Erde aus dem All mit Raumstation am rechten Rand">
      <defs>
        <linearGradient id="orbit" x1="0" y1="0" x2="0.3" y2="1">
          <stop offset="0" stop-color="#0b0f14"/>
          <stop offset=".25" stop-color="#5d6f80"/>
          <stop offset=".5" stop-color="#3b4a58"/>
          <stop offset="1" stop-color="#121518"/>
        </linearGradient>
      </defs>
      <polygon points="0,232 560,92 560,792 0,792" fill="url(#orbit)"/>
    </svg>
    <div class="brand-name">Hollweck &amp; Feist</div>
    <h1 class="cover__title"><span class="accent">Softwarelösungen</span> für<br>digitale Unternehmens-<br>prozesse</h1>
  </div>
</section>

<section class="stage stage--spread">
  <div class="spread">
    <div class="page page--left">
      <svg class="fill" width="420" height="594" role="img" aria-label="Start einer Raumfähre am Startturm mit Rauchwolken">
        <defs>
          <linearGradient id="launch" x1="0" y1="0" x2="0" y2="1">
            <stop offset="0" stop-color="#5c83b4"/>
            <stop offset=".45" stop-color="#b7c6d6"/>
            <stop offset=".7" stop-color="#c9a878"/>
            <stop offset="1" stop-color="#d9dbdc"/>
          </linearGradient>
        </defs>
        <rect width="420" height="594" fill="url(#launch)"/>
      </svg>
    </div>
    <div class="page page--right">
      <svg class="fill" width="420" height="594" role="img" aria-label="Fortsetzung des Himmels über dem Startplatz">
        <defs>
          <linearGradient id="sky" x1="0" y1="0" x2="0" y2="1">
            <stop offset="0" stop-color="#28323f"/>
            <stop offset=".5" stop-color="#4f6c92"/>
            <stop offset="1" stop-color="#a9adb1"/>
          </linearGradient>
        </defs>
        <rect width="420" height="594" fill="url(#sky)"/>
        <polygon points="222,0 420,0 420,594 62,594" fill="#fff"/>
      </svg>
      <p class="intro__text">Kommen Sie mit<br>auf unsere digitale<br>Arche Noah in<br>die Zukunft des<br><span class="accent">Projektmanagements!</span></p>
      <div class="brand-name partner partner--tivo">tivonet</div>
      <div class="brand-name partner partner--hf">Hollweck &amp; Feist</div>
    </div>
  </div>
</section>

<section class="stage stage--spread">
  <div class="spread">
    <div class="page page--left">
      <svg class="fill" width="420" height="594">
        <defs>
          <linearGradient id="bear" x1="0" y1="0" x2="1" y2="1">
            <stop offset="0" stop-color="#4d4c45"/>
            <stop offset=".5" stop-color="#8a5a34"/>
            <stop offset="1" stop-color="#5a5f58"/>
          </linearGradient>
        </defs>
        <rect width="420" height="280" fill="url(#bear)" role="img" aria-label="Porträt eines Braunbären"/>
        <polygon points="0,238 420,272 420,594 0,594" fill="var(--green)"/>
      </svg>
      <div class="product" style="top:292px">
        <h2 class="product__name">Steady Bear</h2>
        <p class="product__lead">Einfaches planen und steuern großer Projekt-<br>portfolios und komplexer Programme</p>
        <div class="product__body">
          <p>Steady Bear ist die Lösung für ein erfolgreiches Projekt-, Programm- und Portfoliomanagement, welche technisch auf Veltrona Plan Server/Online basiert. Das zukunftsorientierte Tool hilft großen Unternehmen bei der Planung und Steuerung ihrer Projekte.</p>
          <p>Steady Bear aggregiert Projektinformationen auf verschiedenen Ebenen und ermöglicht eine Kollaboration und Eskalation zwischen Projekten und unterschiedlichen Hierarchieebenen.</p>
        </div>
      </div>
    </div>
    <div class="page page--right page--panel">
      <div class="card" style="top:36px;height:140px">
        <p class="card__text">Portfolio, Program &amp; Project Coordination Tool – Q³PT State-of-art Know How</p>
        <svg class="card__art" width="200" height="120">
          <polygon points="40,2 60,2 70,118 30,118" fill="#e3f1d2"/>
          <line x1="88" y1="8" x2="88" y2="112" stroke="var(--line)"/>
          <text class="mini" x="40" y="25">Portfolio</text>
          <text class="mini" x="36" y="60">Programm</text>
          <text class="mini" x="38" y="100">Projekt</text>
          <text class="mini" x="100" y="45">Plan Sicht</text>
          <text class="mini" x="140" y="22">Zentrale Steuerung</text>
          <g fill="none" stroke="var(--green)" stroke-width="4">
            <circle cx="120" cy="66" r="8"/><circle cx="148" cy="60" r="11"/><circle cx="175" cy="68" r="8"/>
          </g>
          <line x1="95" y1="84" x2="195" y2="84" stroke="var(--green)" stroke-dasharray="2 2"/>
          <text class="mini" x="130" y="100">Gemeinsame Daten</text>
        </svg>
      </div>
      <div class="card" style="top:190px;height:130px">
        <p class="card__text">Portfolio, Program &amp; Project Coordination –<br>Q³PT Startkonfiguration und Individualanpassungen</p>
        <svg class="card__art" width="200" height="112">
          <line x1="20" y1="8" x2="20" y2="86" stroke="var(--line)"/>
          <line x1="20" y1="86" x2="196" y2="86" stroke="var(--line)"/>
          <polygon points="22,84 120,56 120,84" fill="var(--green)"/>
          <polygon points="120,56 180,52 180,84 120,84" fill="#e3f1d2"/>
          <polyline points="22,40 180,30" fill="none" stroke="#c9c9c9"/>
          <circle cx="180" cy="30" r="2" fill="#f0b400"/>
          <text class="mini" x="110" y="24">Kosten ohne Vorlage</text>
          <text class="mini" x="140" y="72">Hollweck &amp; Feist</text>
          <text class="mini" x="30" y="98">Start</text>
          <text class="mini" x="90" y="98">Q³PT Basis</text>
          <text class="mini" x="150" y="98">Anpassung</text>
        </svg>
      </div>
      <div class="card" style="top:334px;height:176px">
        <div class="card__text" style="top:24px">Basis: Veltrona Plan Server und TeamDeck
          <ul><li>standardisierte Lösung für unternehmensweites Multiprojektmanagement in Veltrona EPM Umgebung</li><li>beste Integration in Deskline Anwendungen</li></ul>
        </div>
        <svg class="card__art" width="200" height="160">
          <g fill="var(--green)"><rect x="20" y="6" width="8" height="8"/><rect x="50" y="38" width="12" height="12"/><rect x="50" y="88" width="8" height="8"/><rect x="50" y="140" width="8" height="8"/></g>
          <circle cx="86" cy="10" r="5" fill="#4a90c8"/>
          <text class="mini" x="32" y="12">Plan Professional</text>
          <text class="mini" x="66" y="47" style="font-size:9px">Q³PT</text>
          <text class="mini" x="62" y="94">Plan Server</text>
          <text class="mini" x="62" y="120">TeamDeck</text>
          <text class="mini" x="62" y="146">Basis Server</text>
          <g stroke="var(--green)" fill="none"><line x1="56" y1="16" x2="56" y2="36"/><line x1="56" y1="52" x2="56" y2="86"/><line x1="56" y1="98" x2="56" y2="138"/></g>
          <g fill="#eeeeee"><rect x="150" y="4" width="40" height="10" rx="2"/><rect x="150" y="30" width="40" height="10" rx="2"/><rect x="150" y="56" width="40" height="10" rx="2"/><rect x="150" y="82" width="40" height="10" rx="2"/><rect x="150" y="108" width="40" height="10" rx="2"/><rect x="150" y="134" width="40" height="10" rx="2"/></g>
        </svg>
      </div>
    </div>
  </div>
</section>

<section class="stage stage--spread">
  <div class="spread">
    <div class="page page--left">
      <svg class="fill" width="420" height="594">
        <defs>
          <linearGradient id="lion" x1="0" y1="0" x2="1" y2="1">
            <stop offset="0" stop-color="#5a4a3a"/>
            <stop offset=".45" stop-color="#b8692a"/>
            <stop offset="1" stop-color="#8f8a80"/>
          </linearGradient>
        </defs>
        <rect width="420" height="280" fill="url(#lion)" role="img" aria-label="Porträt eines Löwen mit Mähne"/>
        <polygon points="0,238 420,272 420,594 0,594" fill="var(--green)"/>
      </svg>
      <div class="product" style="top:292px">
        <h2 class="product__name">Bright Lion</h2>
        <p class="product__lead">Einfache und transparente Projektabbildung<br>und -abwicklung in TeamDeck</p>
        <div class="product__body">
          <p>Bright Lion erweitert den bestehenden Standard Funktionsumfang von Veltrona TeamDeck um Fähigkeiten für ein echtes Multiprojektmanagement.</p>
          <p>Im Fokus stehen dabei Bedienbarkeit, Echtzeit-Controlling und Kosteneffizienz. Bright Lion ist die optimale Lösung für die professionelle Projektverwaltung von mittleren und großen Unternehmen.</p>
        </div>
      </div>
    </div>
    <div class="page page--right page--panel">
      <div class="card" style="top:36px;height:460px">
        <div class="bullets">
          <ul><li>Schnelle Transparenz: einfach und transparent Projekte abbilden</li><li>für mittelgroße &amp; große Unternehmen</li></ul>
          <ul><li>Überwachung aller projektgefährdender Risiken</li><li>Ready To use</li></ul>
        </div>
        <svg style="position:absolute;left:20px;top:96px" width="300" height="340">
          <rect width="300" height="8" fill="#e3f1d2"/>
          <rect x="0" y="12" width="90" height="90" fill="#f7f7f7"/>
          <g fill="#4a90c8"><rect x="6" y="20" width="30" height="4"/><rect x="10" y="30" width="60" height="2"/><rect x="10" y="36" width="50" height="2"/><rect x="10" y="42" width="64" height="2"/><rect x="10" y="48" width="40" height="2"/></g>
          <g fill="#999"><rect x="100" y="22" width="70" height="6"/></g>
          <rect x="100" y="36" width="30" height="5" fill="#4a90c8"/>
          <g fill="#d9534f"><rect x="100" y="60" width="40" height="2"/><rect x="100" y="66" width="50" height="2"/><rect x="100" y="72" width="36" height="2"/><rect x="100" y="78" width="44" height="2"/></g>
          <circle cx="150" cy="16" r="4" fill="#d9534f"/><circle cx="230" cy="16" r="4" fill="var(--green)"/><circle cx="280" cy="16" r="4" fill="#f0b400"/>
          <g fill="#cccccc"><rect x="0" y="112" width="300" height="1"/><rect x="0" y="140" width="300" height="1"/><rect x="0" y="170" width="300" height="1"/><rect x="0" y="200" width="300" height="1"/></g>
          <g fill="#c5d8ea"><rect x="0" y="142" width="300" height="4"/><rect x="0" y="172" width="300" height="4"/><rect x="0" y="204" width="300" height="4"/><rect x="0" y="238" width="300" height="5"/></g>
          <g fill="#e2e2e2"><rect x="0" y="150" width="300" height="14"/><rect x="0" y="180" width="300" height="14"/><rect x="0" y="212" width="300" height="20"/><rect x="0" y="246" width="300" height="80"/></g>
          <g fill="var(--green)"><circle cx="250" cy="256" r="2"/><circle cx="262" cy="266" r="2"/><circle cx="274" cy="276" r="2"/><circle cx="250" cy="296" r="2"/></g>
          <g fill="#d9534f"><circle cx="262" cy="286" r="2"/><circle cx="274" cy="306" r="2"/></g>
        </svg>
      </div>
    </div>
  </div>
</section>

</body>
</html>
```